LumaguardUSA /The Brightmore & Brightmore X

Bringing to market a revolutionay new products. UVC sanitizing machines have been used by hospitals for years in operating rooms to kill viruses and bacteria. The problem is those machines cost anywhere for $65,000 to $125,000 each machine making the proven very effective technology unavailable to most industires that need them We have made 2 models that use the exact same effective technolgy that are very affordable. Our main product is The Brightmore. Tis machine is a mobile 216w unit that can effectively treat up to 1500sq ft and kill 99.9% of viruses (Covid and bacteria in 30 minutes. This unit can be used in areas such as schools, churches, nursing homes, daycares, resturaunts, casinos(especially casino bathrooms). offices, public transport, planes, vacational Rentals, etc.
Our smaller compact but powerful unit The Brightmore X is compact and powerful and can treat areas up to 864 sq ft. this unit is for use in hotel rooms, cruise ship cabins, Ambulances, School buses, and other small areas.
We all have been seeing people using sprayers spraying unknown and untested chemicals all over surfaces. there has been no long term testing and all I can picture is kids touching these surfaces and putting their fingers in their mouths. In years this will be the asbestos, weedaway and talcum powder in the near future.
These machines eliminate the risk of those chemicals. Are completly safe and have been used by major medical facilities for years.
I am looking for a website to promote and sell these 2 products. We need to market to all the prospective types of clients that could use these and show their own customers how they have responsibly took action in tried and true technology to protect them.
The main company for these products is LumaguardUSA. We are also going to be selling this side of the business as a service business where we are looking for partners around the U.S to join our team to be able to provide UVC cleaning to clients that would rather call a professionla service to come out and sanitize their location rathe than having staff do this on their own.
Looking for the basics of a website design with a simple page where they can purchase the machines. We currently have a facebook page contest that is near end with great designs. I will attach those or links in the coming days. I need this all done, setup and hosted with the ability to have constant updates. I no absolutely know anything about coding. I can add on a constant basis wording, descriptions etc. whatever is needed.
I will upload more pictures daily.
Update- Here is some boi info for site.
About The Brightmore.
UV germicidal is limited to a single wavelength of UV-C at 253.7nm. The Brightmore 360 technology is a 216w system built to produce the very effective range with an extensive range of germicidal UVC. This extended range delivers a germicidal intensity that penetrates the cell walls of microorganisms and causes irreparable damage. That’s what makes our high Intensity mobile UVC Brightmore Machine so extremely fast and effective at reducing microbial loads like the Covid Virus.

Large Medical facilities have been using this same technology in operating rooms for years but at a cost of $65k-$125k

We have taken that same technolgy and built a system that any business or School system can use the same proven and effective technology at a price they can afford.

Why The Brightmore?

Manual cleaning leaves on average 47% of surface areas untouched. The Brightmore ensures those areas are sanitized.
No more of spraying harmful or long term untested chemicals need to be sprayed. Much like the Asbestos, weedaway and talcum powders of the past.
An extremely fast and effective addition to your cleaning & sanitzing schedule.

Time Matters!

Every second counts when you feel your school or business may have a possible issue. Roll out The Brightmore and start killing it immediately. No need to wait for staff, chemicals or delays. Set up in just minutes. Clear the area and turn it on. The Brightmore gets to work immediatley.

About US .

LumaguardUSA/The Brightmore was founded in early 2020 as the emmergence of Covid-19 began. CEO/Owner- Dale Pemberton with a over 16 yrs. in the LED lighting field has used his experience in lighting to create a reasonable priced product and service to help the everyday school or business. With years of being around and involved with all types of lighting including Germicidal lamps in Hospital settings
he created the very expensive alternative that can be used by thousands of industries to help and slow down this deadly Virus.

"Our Motto" Any technology that is available to assist should not be limited by price.

Target Market(s)

Schools both public and private, hotels, Vacation rentals, daycares, nursing homes, casinos, cruise lines

```html
<!DOCTYPE html>
<html lang="en">
<head>
<meta charset="utf-8">
<title>LumaguardUSA – The Brightmore</title>
<link href="https://fonts.googleapis.com/css2?family=Poppins:wght@400;500;600;700&display=swap" rel="stylesheet">
<style>
:root{
  --stage:#0b2a4a;
  --navy:#004a7c;
  --navy-deep:#003b66;
  --sky:#0aa0f0;
  --accent:#1e9be8;
  --light-band:#bac7e4;
  --ink:#1d2a3a;
  --muted:#4a5a6e;
  --red:#c21a2c;
  --white:#ffffff;
}
*{margin:0;padding:0;box-sizing:border-box}
html,body{width:954px;height:1200px;overflow:hidden}
body{background:var(--stage);font-family:'Poppins',sans-serif;color:var(--ink);position:relative}
.page{position:absolute;left:127px;top:42px;width:700px;height:1116px;background:var(--white);overflow:hidden}
.abs{position:absolute}

/* top bar */
.topbar{left:0;top:0;width:700px;height:13px;background:var(--navy)}
.topbar .contact{left:135px;top:0;height:13px;display:flex;align-items:center;gap:8px;font-size:4.5px;color:var(--white);font-weight:500}
.topbar .contact span{display:flex;align-items:center;gap:2px}
.topbar .social{right:131px;top:3px;display:flex;gap:3px}
.topbar .social i{display:block;width:7px;height:7px;border-radius:50%;background:var(--white)}

/* header */
.header{left:0;top:13px;width:700px;height:49px;background:var(--white)}
.brand{left:134px;top:17px;display:flex;gap:14px;align-items:center;font-size:9px;font-weight:700;color:var(--navy)}
.brand .dot{display:inline-block;width:7px;height:7px;border-radius:50%;background:var(--red);margin-right:3px;vertical-align:middle}
.nav{left:394px;top:20px;display:flex;gap:9px;font-size:5.5px;font-weight:600;color:var(--ink)}
.nav a{color:inherit;text-decoration:none;position:relative}
.nav a.active{color:var(--navy)}
.nav a.active:after{content:"";position:absolute;left:0;right:0;bottom:-3px;height:1px;background:var(--accent)}
.cart{left:554px;top:20px;display:flex;align-items:center;gap:1px}
.cart b{width:5px;height:5px;border-radius:50%;background:var(--accent);display:block}

/* hero */
.hero{left:0;top:62px;width:700px;height:253px;background:radial-gradient(ellipse 260px 200px at 480px 130px,#1a6fe0 0%,#0c3e8e 40%,#050b1c 80%,#020409 100%)}
.hero .kicker{left:122px;top:54px;font-size:7.5px;font-weight:600;color:var(--white)}
.hero h1{left:122px;top:73px;width:280px;font-size:15px;line-height:21px;font-weight:500;color:var(--white)}
.hero p{left:122px;top:120px;width:210px;font-size:5.2px;line-height:11px;color:var(--white);font-weight:500}
.btn{left:123px;top:158px;width:59px;height:18px;background:var(--accent);color:var(--white);font-size:5.8px;font-weight:600;display:flex;align-items:center;justify-content:center}
.arrow{width:15px;height:15px;background:rgba(255,255,255,.35);top:118px;display:flex;align-items:center;justify-content:center}
.hero .prev{left:7px}
.hero .next{left:678px}
.hero-product{left:385px;top:16px;width:170px;height:214px;border-radius:10px;background:linear-gradient(180deg,#6cc4ff 0%,#3a8fe8 45%,#e6eef7 75%,#b8c6d6 100%);opacity:.85}

/* features */
.features{left:0;top:315px;width:700px;height:114px;background:var(--white)}
.feature{top:34px;width:139px;height:68px;border:1px solid var(--navy);display:flex;align-items:center;justify-content:center;text-align:center;padding:10px 12px 0;font-size:5.5px;line-height:9px;color:var(--muted)}
.feature .badge{position:absolute;left:50%;top:-17px;margin-left:-16px;width:32px;height:32px;border-radius:50%;background:var(--white);border:2px solid var(--red);display:flex;align-items:center;justify-content:center}
.feature .badge span{width:24px;height:24px;border-radius:50%;background:var(--navy);display:flex;align-items:center;justify-content:center}

/* about */
.about{left:0;top:429px;width:700px;height:170px;background:var(--light-band)}
.about-product{left:177px;top:21px;width:48px;height:104px;border-radius:4px;background:linear-gradient(180deg,#cfe6fb 0%,#9fc3e8 45%,#f4f6f9 70%,#c9cfd7 100%)}
.about h2{left:281px;top:10px;font-size:11px;font-weight:600;color:var(--ink)}
.about h2 em,.why h2 em{font-style:normal;font-weight:400;color:var(--accent)}
.about .copy{left:281px;top:29px;width:286px;font-size:5.3px;line-height:10.2px;color:var(--muted)}
.about .copy p+p{margin-top:12px}
.about .copy strong{color:var(--ink);font-weight:600}

/* why */
.why{left:0;top:598px;width:700px;height:261px;background:var(--navy)}
.why h2{left:0;width:700px;top:48px;text-align:center;font-size:11px;font-weight:600;color:var(--white)}
.why .copy{left:131px;top:81px;width:290px;font-size:5.3px;line-height:10.2px;color:var(--white)}
.why .copy p{margin-bottom:3px}
.why .copy p.gap{margin-top:12px}
.why-product{left:461px;top:86px;width:56px;height:105px;border-radius:4px;background:linear-gradient(180deg,#e9eef4 0%,#aab7c6 50%,#f2f4f7 80%,#c3ccd6 100%);opacity:.9}
.totop{width:12px;height:12px;background:var(--navy-deep);display:flex;align-items:center;justify-content:center}
.why .totop{left:683px;top:18px}

/* time */
.time{left:0;top:859px;width:700px;height:71px;background:var(--sky);text-align:center;color:var(--white)}
.time h2{margin-top:13px;font-size:12px;font-weight:600}
.time p{width:440px;margin:6px auto 0;font-size:5.3px;line-height:10px}

.rule{left:131px;top:942px;width:438px;height:1px;background:#9fb6cc}

/* footer */
.footer{left:0;top:970px;width:700px;height:132px;background:var(--navy);color:var(--white)}
.footer .brands{left:131px;top:12px;display:flex;gap:7px;font-size:6px;font-weight:700}
.footer h3{font-size:7.5px;font-weight:600}
.footer .about-f{left:131px;top:43px;width:140px}
.footer .about-f p{font-size:5.3px;line-height:8px}
.footer .links{left:281px;top:9px}
.footer .links ul{list-style:none;margin:3px 0 0 9px;font-size:5.3px}
.footer .links li{height:13.6px}
.footer .contact-f{left:430px;top:9px;font-size:5.3px}
.footer .contact-f h4{font-size:5.5px;font-weight:600;margin-top:12px}
.footer .contact-f h4:first-of-type{margin-top:1px}
.footer .contact-f div{display:flex;align-items:center;gap:2px;margin-top:3px}

.bottombar{left:0;top:1102px;width:700px;height:14px;background:var(--red);color:var(--white);font-size:4.5px}
.bottombar .copy{left:131px;top:4px}
.bottombar .legal{right:131px;top:4px;display:flex;gap:7px}
.bottombar .totop{left:683px;top:1px;background:transparent}
</style>
</head>
<body>
<div class="page">

  <div class="abs topbar">
    <div class="abs contact">
      <span><svg width="5" height="5" viewBox="0 0 10 10"><path d="M2 1l2 2-1 1.5c.8 1.5 1.8 2.5 3.5 3.5L8 7l2 2-1.5 1C4.5 9.5.5 5.5 1 1.5z" fill="#fff"/></svg>011 555 0147</span>
      <span><svg width="6" height="5" viewBox="0 0 12 9"><rect x="0" y="0" width="12" height="9" fill="#fff"/><path d="M0 0l6 5 6-5" stroke="#004a7c" fill="none"/></svg>sales@example.com</span>
    </div>
    <div class="abs social"><i></i><i></i><i></i><i></i></div>
  </div>

  <header class="abs header">
    <div class="abs brand">
      <span><span class="dot"></span>LumaguardUSA</span>
      <span>Brightmore</span>
      <span>Brightmore X</span>
    </div>
    <nav class="abs nav"><a class="active">Home</a><a>About</a><a>Shop</a><a>Contact Us</a></nav>
    <div class="abs cart"><svg width="7" height="6" viewBox="0 0 14 12"><path d="M0 1h3l2 7h7l2-5H4" fill="none" stroke="#004a7c" stroke-width="1.6"/><circle cx="6" cy="10.5" r="1.2" fill="#004a7c"/><circle cx="11" cy="10.5" r="1.2" fill="#004a7c"/></svg><b></b></div>
  </header>

  <section class="abs hero">
    <div class="abs kicker">About the Brightmore</div>
    <h1 class="abs">UV germicidal is limited to a single wavelength of UV-C at 253.7nm</h1>
    <p class="abs">The Brightmore 360 technology is a 216w system built to produce the very effective range with an extensive range of germicidal UVC</p>
    <div class="abs btn">Shop Now</div>
    <div class="abs hero-product" role="img" aria-label="Photo of the mobile Brightmore UVC machine and the compact Brightmore X lamp glowing blue"></div>
    <div class="abs arrow prev"><svg width="5" height="6" viewBox="0 0 5 8"><path d="M4 1L1 4l3 3" stroke="#fff" fill="none"/></svg></div>
    <div class="abs arrow next"><svg width="5" height="6" viewBox="0 0 5 8"><path d="M1 1l3 3-3 3" stroke="#fff" fill="none"/></svg></div>
  </section>

  <section class="abs features">
    <div class="abs feature" style="left:131px">
      <div class="badge"><span><svg width="14" height="10" viewBox="0 0 14 10"><path d="M1 2q1.5-1.5 3 0t3 0 3 0 3 0M1 5q1.5-1.5 3 0t3 0 3 0 3 0M1 8q1.5-1.5 3 0t3 0 3 0 3 0" stroke="#fff" fill="none" stroke-width="1"/></svg></span></div>
      UV germicidal is limited to a single wavelength of UV-C at 253.7nm
    </div>
    <div class="abs feature" style="left:281px">
      <div class="badge"><span><svg width="16" height="16" viewBox="0 0 16 16"><circle cx="8" cy="8" r="6.5" stroke="#fff" fill="none" stroke-width=".8"/><text x="8" y="9.8" font-size="5" font-family="Poppins,sans-serif" font-weight="700" fill="#fff" text-anchor="middle">360</text></svg></span></div>
      The Brightmore 360 technology a 216w system built to produce the very effective range with an extensive range of germicidal UVC.
    </div>
    <div class="abs feature" style="left:430px">
      <div class="badge"><span><svg width="14" height="14" viewBox="0 0 14 14"><circle cx="7" cy="7" r="3.2" fill="#fff"/><path d="M7 1v3M7 10v3M1 7h3M10 7h3M2.8 2.8l2 2M9.2 9.2l2 2M2.8 11.2l2-2M9.2 4.8l2-2" stroke="#fff" stroke-width="1"/></svg></span></div>
      Extremely fast and effective at reducing microbial loads like the Covid Virus
    </div>
  </section>

  <section class="abs about">
    <div class="abs about-product" role="img" aria-label="Photo of the Brightmore mobile UVC machine"></div>
    <h2 class="abs">About the <em>Brightmore</em></h2>
    <div class="abs copy">
      <p>UV germicidal is limited to a single wavelength of UV-C at 253.7nm. The Brightmore 360 technology is a 216w system built to produce the very effective range with an extensive range of germicidal UVC. This extended range delivers a germicidal intensity that penetrates the cell walls of microorganisms and causes irreparable damage. That's what makes our high Intensity mobile UVC Brightmore Machine so extremely fast and effective at reducing microbial loads like the Covid Virus.</p>
      <p><strong>Large Medical facilities have been using this same technology in operating rooms for years but at a cost of $65k-$125k</strong></p>
      <p>We have taken that same technology and built a system that any business or School system can use the same proven and effective technology at a price they can afford.</p>
    </div>
  </section>

  <section class="abs why">
    <div class="abs totop"><svg width="6" height="6" viewBox="0 0 8 8"><path d="M4 7V1M1 4l3-3 3 3" stroke="#fff" fill="none"/></svg></div>
    <h2 class="abs">Why The <em>Brightmore?</em></h2>
    <div class="abs copy">
      <p>Manual cleaning leaves on average 47% of surface areas untouched. The Brightmore ensures those areas are sanitized.</p>
      <p>No more of spraying harmful or long term untested chemicals need to be sprayed. Much like the Asbestos, weedaway and talcum powders of the past.</p>
      <p>An extremely fast and effective addition to your cleaning &amp; sanitizing schedule.</p>
      <p class="gap">We have taken that same technology and built a system that any business or School system can use the same proven and effective technology at a price they can afford.</p>
    </div>
    <div class="abs why-product" role="img" aria-label="Photo of the compact Brightmore X UVC lamp"></div>
  </section>

  <section class="abs time">
    <h2>Time Matters!</h2>
    <p>Every second counts when you feel your school or business may have a possible issue. Roll out the Brightmore and start killing it immediately. No need to wait for staff, chemicals or delays. Set up in just minutes. Clear the area and turn it on. The Brightmore gets to work immediatley.</p>
  </section>

  <div class="abs rule"></div>

  <footer class="abs footer">
    <div class="abs brands"><span>LumaguardUSA</span><span>Brightmore</span><span>Brightmore X</span></div>
    <div class="abs about-f">
      <h3>About The Brightmore</h3>
      <p>UV germicidal is limited to a single wavelength of UV-C at 253.7nm. The Brightmore 360 technology is a 216w system built to produce the very effective range with an extensive range of germicidal UVC.</p>
    </div>
    <div class="abs links">
      <h3>Usefull Links</h3>
      <ul><li>About</li><li>Shop</li><li>Contact Us</li></ul>
    </div>
    <div class="abs contact-f">
      <h3>Contact us</h3>
      <h4>Address</h4>
      <div><svg width="4" height="5" viewBox="0 0 8 10"><path d="M4 10C1 6 0 5 0 4a4 4 0 018 0c0 1-1 2-4 6z" fill="#fff"/></svg>1450, Harbor Point Drive FL 33400 United States</div>
      <h4>Phone</h4>
      <div><svg width="5" height="5" viewBox="0 0 10 10"><path d="M2 1l2 2-1 1.5c.8 1.5 1.8 2.5 3.5 3.5L8 7l2 2-1.5 1C4.5 9.5.5 5.5 1 1.5z" fill="#fff"/></svg>+1 555 010 2345</div>
      <h4>Email</h4>
      <div><svg width="5" height="4" viewBox="0 0 12 9"><rect width="12" height="9" fill="#fff"/><path d="M0 0l6 5 6-5" stroke="#004a7c" fill="none"/></svg>info@example.net</div>
    </div>
  </footer>

  <div class="abs bottombar">
    <div class="abs copy">© 2020 Brightmore | All Right Reserved.</div>
    <div class="abs legal"><span>Privacy Policy</span><span>Terms &amp; Conditions</span></div>
    <div class="abs totop"><svg width="6" height="6" viewBox="0 0 8 8"><path d="M4 7V1M1 4l3-3 3 3" stroke="#fff" fill="none"/></svg></div>
  </div>

</div>
</body>
</html>
```